Looking for a professional, clean and crisp business card

I am in the underground utilities industry and am just looking for a really impressive business card. I would like our card to be white with our symbol crisp and clear with it protruding. I also have a business partner that will require his name and info on the card once the design is set. I would like to have our website info on the card which is;
http://granitetrenchco.example/

Contact Information for Business Card

Website, contact name, number and email

```html
<!DOCTYPE html>
<html lang="en">
<head>
<meta charset="utf-8">
<title>Granite Trench Co — Business Card</title>
<link rel="stylesheet" href="https://fonts.googleapis.com/css2?family=Roboto+Condensed:wght@400;700&display=swap">
<style>
  :root {
    --backdrop: #6a6a6a;
    --card-light: #ffffff;
    --card-dark: #221f20;
    --ink: #231f20;
    --accent-blue: #3a5ba8;
    --paper-text: #ffffff;
  }
  * { margin: 0; padding: 0; box-sizing: border-box; }
  html, body {
    width: 1065px;
    height: 1200px;
    overflow: hidden;
    background: var(--backdrop);
    font-family: "Roboto Condensed", "Arial Narrow", sans-serif;
  }
  .canvas {
    position: relative;
    width: 1065px;
    height: 1200px;
  }
  .card {
    position: absolute;
    height: 363px;
  }
  .card--front {
    left: 292px;
    top: 218px;
    width: 583px;
    background: var(--card-light);
    border-radius: 0 181.5px 181.5px 0;
    color: var(--ink);
  }
  .card--back {
    left: 263px;
    top: 623px;
    width: 582px;
    background: var(--card-dark);
    border-radius: 181.5px 0 0 181.5px;
  }
  .person {
    position: absolute;
    left: 30px;
    top: 56px;
  }
  .person__name {
    font-weight: 700;
    font-size: 23px;
    line-height: 1;
    letter-spacing: 0.2px;
  }
  .person__role {
    font-size: 19px;
    line-height: 1;
    margin-top: 4px;
    color: var(--accent-blue);
  }
  .contacts {
    position: absolute;
    left: 31px;
    top: 242px;
    list-style: none;
  }
  .contacts__item {
    display: flex;
    align-items: center;
    gap: 8px;
    height: 22.5px;
    font-size: 18.5px;
  }
  .contacts__icon {
    width: 18px;
    height: 18px;
    flex: none;
  }
  .wordmark {
    position: absolute;
    transform: translate(-50%, -50%);
    text-align: center;
    font-weight: 700;
    font-size: 34px;
    line-height: 1.05;
    text-transform: uppercase;
    letter-spacing: 1px;
  }
  .card--front .wordmark { left: 391px; top: 181px; color: var(--ink); }
  .card--back .wordmark { left: 291px; top: 181px; color: var(--paper-text); }
</style>
</head>
<body>
<main class="canvas">
  <section class="card card--front" aria-label="Business card front">
    <div class="person">
      <h1 class="person__name">MARCUS HALE</h1>
      <p class="person__role">Managing Director</p>
    </div>
    <ul class="contacts">
      <li class="contacts__item">
        <svg class="contacts__icon" viewBox="0 0 24 24" aria-hidden="true">
          <path d="M6.6 10.8a15 15 0 0 0 6.6 6.6l2.2-2.2a1 1 0 0 1 1-.25 11.4 11.4 0 0 0 3.6.57 1 1 0 0 1 1 1V20a1 1 0 0 1-1 1A17 17 0 0 1 3 4a1 1 0 0 1 1-1h3.5a1 1 0 0 1 1 1c0 1.25.2 2.45.57 3.6a1 1 0 0 1-.25 1z" fill="var(--ink)"/>
          <path d="M14 3a7 7 0 0 1 7 7M14 6.5a3.5 3.5 0 0 1 3.5 3.5" fill="none" stroke="var(--ink)" stroke-width="1.8"/>
        </svg>
        <span>055-210 384 617</span>
      </li>
      <li class="contacts__item">
        <svg class="contacts__icon" viewBox="0 0 24 24" aria-hidden="true">
          <rect x="2" y="5" width="20" height="14" fill="var(--ink)"/>
          <path d="M2.5 5.5 12 13l9.5-7.5M2.5 18.5l7-6M21.5 18.5l-7-6" fill="none" stroke="#fff" stroke-width="1.3"/>
        </svg>
        <span>info@granitetrenchco.example</span>
      </li>
      <li class="contacts__item">
        <svg class="contacts__icon" viewBox="0 0 24 24" aria-hidden="true">
          <g fill="none" stroke="var(--ink)" stroke-width="1.8">
            <circle cx="12" cy="12" r="9.5"/>
            <ellipse cx="12" cy="12" rx="4.2" ry="9.5"/>
            <path d="M2.5 12h19M4 7h16M4 17h16M12 2.5v19"/>
          </g>
        </svg>
        <span>www.granitetrenchco.example</span>
      </li>
    </ul>
    <p class="wordmark">Granite<br>Trench Co</p>
  </section>

  <section class="card card--back" aria-label="Business card back">
    <p class="wordmark">Granite<br>Trench Co</p>
  </section>
</main>
</body>
</html>
```